I'd like a business card that makes my company, Fenwright Marsh Associates Ltd stand out from the normal financial & IT services sector . It would be great to have a card that a potential client will think "wow" this is out of the norm , I'll give these guys a call. My business aims to provide consultancy services for financial and IT institutions but I'm looking to provide a newer approach that fits into today's social media rather than the standard "big 4" approach. My business helps companies assess their internal issues and aims to solve issues via business process re-engineering. The final design should have a balance of the maturity of the financial & IT sector with the fresh approach of the thriving social media sector

Target Market(s)

Business Managers and Directors, technical Managers and directors. Aged between 20 and 60 that handle project budgets

Industry/Entity Type

Financial

Requirements
Must have
• Must incorporate company logo currently being designed
Should not have
• No old-style fonts please.

```html
<!DOCTYPE html>
<html lang="en">
<head>
<meta charset="utf-8">
<title>Fenwright Marsh Associates Ltd — Business Card</title>
<link rel="stylesheet" href="https://fonts.googleapis.com/css2?family=PT+Sans:ital,wght@0,400;0,700;1,400&display=swap">
<style>
  :root {
    --backdrop: #c9c9cb;
    --purple: #9c2a6c;
    --orange: #ec6b2d;
    --paper: #f7f7f6;
    --ink: #555459;
    --rule: #9a9a9e;
    --white: #ffffff;
  }
  * { margin: 0; padding: 0; box-sizing: border-box; }
  html, body {
    width: 1200px; height: 1000px; overflow: hidden;
    background: var(--backdrop);
    font-family: "PT Sans", sans-serif;
  }
  .canvas { position: relative; width: 1200px; height: 1000px; }

  .card {
    position: absolute;
    width: 525px; height: 300px;
    overflow: hidden;
  }

  /* Front */
  .card-front { left: 110px; top: 120px; background: var(--orange); }
  .front-band {
    position: absolute; left: 0; top: 0; bottom: 0; width: 132px;
    background: var(--purple);
  }
  .front-divider {
    position: absolute; left: 132px; top: 0; bottom: 0; width: 14px;
    background: var(--white);
  }
  .front-brand {
    position: absolute; left: 210px; top: 100px;
    display: flex; align-items: center; gap: 14px;
    color: var(--white);
  }
  .brand-square { width: 44px; height: 44px; background: var(--white); flex: none; }
  .brand-name {
    font-weight: 700; text-transform: uppercase;
    font-size: 21px; line-height: 1.1; letter-spacing: 0.5px;
  }
  .brand-name small { display: block; font-size: 13px; text-transform: none; letter-spacing: 1.5px; }

  /* Back */
  .card-back { left: 565px; top: 560px; background: var(--paper); }
  .back-brand {
    position: absolute; left: 40px; top: 70px;
    display: flex; align-items: center; gap: 10px;
    color: var(--purple);
  }
  .back-brand .brand-square { width: 30px; height: 30px; background: var(--orange); }
  .back-brand .brand-name { font-size: 15px; }
  .back-brand .brand-name small { font-size: 10px; }

  .person {
    position: absolute; right: 40px; top: 64px; width: 200px;
    text-align: right; border-bottom: 1px solid var(--rule); padding-bottom: 6px;
  }
  .person-name { color: var(--purple); font-size: 24px; line-height: 1.1; }
  .person-role { color: var(--orange); font-size: 14px; font-style: italic; font-weight: 700; }

  .contact {
    position: absolute; left: 40px; top: 176px; width: 210px;
    border-top: 1px solid var(--rule); padding-top: 6px;
    color: var(--ink); font-size: 11.5px; line-height: 1.4;
    list-style: none;
  }
  .stripe-purple {
    position: absolute; left: 0; bottom: 0; width: 240px; height: 22px;
    background: var(--purple);
  }
  .stripe-orange {
    position: absolute; left: 240px; right: 0; bottom: 0; top: 176px;
    background: var(--orange);
  }
</style>
</head>
<body>
<main class="canvas">
  <section class="card card-front" aria-label="Business card front">
    <div class="front-band"></div>
    <div class="front-divider"></div>
    <div class="front-brand">
      <span class="brand-square"></span>
      <p class="brand-name">Fenwright Marsh<small>Associates Ltd</small></p>
    </div>
  </section>

  <section class="card card-back" aria-label="Business card back">
    <div class="back-brand">
      <span class="brand-square"></span>
      <p class="brand-name">Fenwright Marsh<small>Associates Ltd</small></p>
    </div>
    <div class="person">
      <p class="person-name">Daniel Hartley</p>
      <p class="person-role">Managing Partner</p>
    </div>
    <ul class="contact">
      <li>48 Calder Row, Brookfield, BF2 7QN, United Kingdom</li>
      <li>555-8821-40</li>
      <li>contact@fenwrightmarsh.com</li>
      <li>www.fenwrightmarsh.com</li>
    </ul>
    <div class="stripe-orange"></div>
    <div class="stripe-purple"></div>
  </section>
</main>
</body>
</html>
```